Entrepreneur Podcast Cover Graphic Design

My wife and I just launched our podcast but we don't like the current cover. We want a new cover designed so it stands out and reflects the professionalism of our podcast. Attached is our current podcast cover design. We'd like to have it read "Rob & Mireya Interview Entrepreneurs on BOLD CROSSROADS" - We'd also like to feature somehow that we have daily tips included.

Target Market(s)

entrepreneurs,business owners,start ups

Industry/Entity Type

Entrepreneur

Font styles to use
Sans Serif

Colors
0355a3
f37122
9bcb3c
fbed22
ec1f27

Requirements
Must have
• Our names listed: Rob & Mireya
Nice to have
• dark, bold colored background with an outline around the edge
Should not have
• no cartoons, no profanity

```html
<!DOCTYPE html>
<html lang="en">
<head>
<meta charset="utf-8">
<title>Rob &amp; Mireya Interview Entrepreneurs on Bold Crossroads</title>
<link rel="stylesheet" href="https://fonts.googleapis.com/css2?family=Marcellus&family=Open+Sans:wght@400;600&display=swap">
<style>
  :root {
    --bg: #000000;
    --orange: #f7962a;
    --blue: #0355a3;
    --blue-light: #4aa8e0;
    --blue-pale: #cfeafb;
    --white: #ffffff;
  }
  html, body {
    margin: 0;
    padding: 0;
    width: 1200px;
    height: 1000px;
    overflow: hidden;
    background: var(--bg);
  }
  .cover {
    display: block;
    width: 1200px;
    height: 1000px;
  }
  .cover__frame {
    fill: none;
    stroke: var(--orange);
    stroke-width: 2;
  }
  .hosts {
    font-family: "Marcellus", serif;
    font-size: 118px;
    fill: var(--orange);
  }
  .tagline {
    font-family: "Open Sans", sans-serif;
    font-weight: 600;
    font-size: 54px;
  }
  .topic-band {
    fill: var(--orange);
  }
  .topic {
    font-family: "Marcellus", serif;
    font-size: 140px;
    fill: var(--blue);
  }
</style>
</head>
<body>
  <svg class="cover" viewBox="0 0 1200 1000" xmlns="http://www.w3.org/2000/svg" role="img" aria-label="Rob &amp; Mireya Interview Entrepreneurs on Bold Crossroads">
    <defs>
      <linearGradient id="hosts-rule-fill" x1="0" y1="0" x2="1" y2="0">
        <stop offset="0" stop-color="var(--orange)" style="stop-color:#f7962a"/>
        <stop offset="0.35" style="stop-color:#f7962a"/>
        <stop offset="0.5" style="stop-color:#ffffff"/>
        <stop offset="0.68" style="stop-color:#f7962a"/>
        <stop offset="1" style="stop-color:#f7962a"/>
      </linearGradient>
      <linearGradient id="tagline-fill" x1="0" y1="0" x2="0" y2="1">
        <stop offset="0" style="stop-color:#4aa8e0"/>
        <stop offset="0.45" style="stop-color:#cfeafb"/>
        <stop offset="1" style="stop-color:#0355a3"/>
      </linearGradient>
    </defs>

    <rect class="cover__frame" x="29" y="204" width="1149" height="643"/>

    <text class="hosts" x="60" y="355" textLength="725" lengthAdjust="spacingAndGlyphs">Rob &amp; Mireya</text>
    <rect x="34" y="372" width="759" height="4" fill="url(#hosts-rule-fill)"/>

    <text class="tagline" x="262" y="488" textLength="721" lengthAdjust="spacingAndGlyphs" fill="url(#tagline-fill)">Interview Entrepreneurs on</text>

    <rect class="topic-band" x="28" y="590" width="1151" height="140"/>
    <text class="topic" x="68" y="712" textLength="1100" lengthAdjust="spacingAndGlyphs">BOLD CROSSROADS</text>
  </svg>
</body>
</html>
```